Business Card Design for Lawn Management

Lawn Management

Industry/Entity Type

Business

Contact Information for Business Card

Calloway Lawn Management
Doran Calloway
Calloway_Lawn@brindlemail.com
404-627-1845

```html
<!DOCTYPE html>
<html lang="en">
<head>
<meta charset="utf-8">
<title>Calloway Lawn Management – Business Card</title>
<link rel="stylesheet" href="https://fonts.googleapis.com/css2?family=Saira+Condensed:wght@600&family=Arimo:wght@400&display=swap">
<style>
  :root {
    --brand-green: #3c9a2e;
    --brand-green-dark: #2f8a24;
    --grass-light: #62bd3c;
    --grass-mid: #49a62f;
    --grass-dark: #34891f;
    --card-white: #ffffff;
    --page-bg: #ffffff;
    --text-green: #3c9a2e;
  }
  * { box-sizing: border-box; margin: 0; padding: 0; }
  html, body {
    width: 1200px; height: 341px; overflow: hidden;
    background: var(--page-bg);
  }
  .sheet { position: relative; width: 1200px; height: 341px; }

  .card { position: absolute; top: 0; width: 594px; height: 341px; overflow: hidden; }
  .card--front { left: 0; }
  .card--back { left: 606px; }

  .grass {
    position: absolute; left: 0; width: 100%;
    background:
      radial-gradient(ellipse at 30% 40%, var(--grass-light) 0%, transparent 60%),
      radial-gradient(ellipse at 75% 70%, var(--grass-light) 0%, transparent 55%),
      linear-gradient(160deg, var(--grass-mid), var(--grass-dark));
  }
  .grass--top { top: 0; height: 45px; }
  .grass--bottom { bottom: 0; height: 47px; }
  .grass--full { top: 0; height: 100%; }

  .front-panel {
    position: absolute; left: 0; top: 45px; width: 100%; height: 249px;
    background: var(--card-white);
    border-top: 9px solid var(--brand-green);
    border-bottom: 7px solid var(--brand-green);
  }

  .brand {
    position: absolute; display: flex; flex-direction: column; align-items: center;
    font-family: "Saira Condensed", "Arial Narrow", sans-serif; font-weight: 600;
    line-height: 1;
  }
  .brand__mark { width: 72px; height: 72px; border-radius: 50%; margin-bottom: 14px; }
  .brand__name { font-size: 42px; letter-spacing: 1px; text-transform: uppercase; }
  .brand__tagline { font-size: 17px; margin-top: 4px; letter-spacing: 0.5px; }

  .brand--front { left: 70px; top: 90px; width: 154px; color: var(--brand-green); }
  .brand--front .brand__mark { background: var(--brand-green); }

  .brand--back { left: 0; top: 84px; width: 100%; color: var(--card-white); }
  .brand--back .brand__mark { background: var(--card-white); }
  .brand--back .brand__name { font-size: 48px; }
  .brand--back .brand__tagline { font-size: 19px; }

  .divider {
    position: absolute; left: 295px; top: 79px; width: 2px; height: 187px;
    background: var(--brand-green);
  }

  .person-name {
    position: absolute; left: 318px; top: 99px;
    font-family: "Saira Condensed", "Arial Narrow", sans-serif; font-weight: 600;
    font-size: 36px; letter-spacing: 1.5px; line-height: 1;
    color: var(--text-green); text-transform: uppercase;
  }

  .contact-list { position: absolute; left: 318px; top: 186px; list-style: none; }
  .contact-item {
    display: flex; align-items: center; height: 20px; margin-bottom: 15px;
    font-family: "Arimo", Arial, sans-serif; font-size: 14px; color: var(--text-green);
  }
  .contact-item svg { width: 16px; height: 16px; margin-right: 14px; flex: none; }
</style>
</head>
<body>
<main class="sheet">

  <section class="card card--front" aria-label="Card front">
    <div class="grass grass--top" role="img" aria-label="Close-up photo of green lawn grass"></div>
    <div class="grass grass--bottom" role="img" aria-label="Close-up photo of green lawn grass"></div>
    <div class="front-panel"></div>

    <div class="brand brand--front">
      <span class="brand__mark" aria-hidden="true"></span>
      <span class="brand__name">Calloway</span>
      <span class="brand__tagline">Lawn Management</span>
    </div>

    <div class="divider" aria-hidden="true"></div>

    <h1 class="person-name">Doran Calloway</h1>

    <ul class="contact-list">
      <li class="contact-item">
        <svg viewBox="0 0 16 16" aria-hidden="true">
          <circle cx="8" cy="8" r="7" fill="none" stroke="var(--brand-green)" stroke-width="1.4"/>
          <path d="M6 4.2c.4 0 .8.9 1 1.4.1.4-.6.8-.5 1.2.3.9 1 1.7 1.8 2 .4.1.8-.6 1.2-.4.5.2 1.3.7 1.3 1.1 0 .7-.9 1.3-1.6 1.3-2.6-.2-4.7-2.4-4.9-5 0-.8.7-1.6 1.7-1.6z" fill="var(--brand-green)"/>
        </svg>
        404-627-1845
      </li>
      <li class="contact-item">
        <svg viewBox="0 0 16 16" aria-hidden="true">
          <rect x="1" y="3.5" width="14" height="10" fill="var(--brand-green)"/>
          <path d="M1 3.5l7 5.5 7-5.5" fill="none" stroke="#fff" stroke-width="1.2"/>
        </svg>
        Calloway_Lawn@brindlemail.com
      </li>
    </ul>
  </section>

  <section class="card card--back" aria-label="Card back">
    <div class="grass grass--full" role="img" aria-label="Close-up photo of green lawn grass"></div>
    <div class="brand brand--back">
      <span class="brand__mark" aria-hidden="true"></span>
      <span class="brand__name">Calloway</span>
      <span class="brand__tagline">Lawn Management</span>
    </div>
  </section>

</main>
</body>
</html>
```